Sales PowerPoint Template to help us attract new customers

We need to create a generic PowerPoint template for our organization. We are in the commercial facilities industry, servicing convenience, restaurants, grocery, and retail customers in the US. We handle trades such as HVAC, Refrigeration, Plumbing, Electrical, Food Equipment, Coffee, etc.

We need to incorporate our new logo, updated colors, Font (Arial). We want it to stand out in this deck and avoid looking like all other facility companies. We want to make sure the template size is not too large (less than 20 MB), so it prevent people to edit/send.
Attached are new logo, colors, old powerpoint template, and finally the "New Design to Incorporate into Template" is new materials we're looking to leverage. This might give you ideas.

Create at least 10 slides (1 cover, 1 agenda slide, at least 7 general slides, and 1 wrap-up slide)

Target Market(s)

Convenience Stores, Retail Stores, Groceries, and Restaurants in the US

Industry/Entity Type

Facilities Services (HVAC, Refrigeration, Plumbing, Electrical, etc, repair and preventative maintenance)

Font styles to use
Other font styles liked:
• Arial

Requirements
Must have
• Follow company colors and font (Arial)
Should not have
• Not approved company colors, font

```html
<!DOCTYPE html>
<html lang="en">
<head>
<meta charset="utf-8">
<title>Norvale Sales Deck Template</title>
<link href="https://fonts.googleapis.com/css2?family=Arimo:wght@400;700&display=swap" rel="stylesheet">
<style>
:root{
  --olive:#8a9440;
  --olive-dark:#3d4418;
  --olive-pale:#f1f2e8;
  --ink:#2a2a2a;
  --grey:#7b7b7b;
  --canvas:#d9dad3;
  --white:#ffffff;
}
*{box-sizing:border-box;margin:0;padding:0}
html,body{width:1200px;height:2629px;overflow:hidden}
body{background:var(--canvas);font-family:Arimo,Arial,sans-serif;color:var(--ink);position:relative}
.slide{position:absolute;width:510px;height:287px;background:var(--white);overflow:hidden;box-shadow:0 2px 6px rgba(0,0,0,.12)}
.slide.olive{background:var(--olive);color:var(--white)}
.col-a{left:76px}.col-b{left:613px}
.r1{top:46px}.r2{top:367px}.r3{top:688px}.r4{top:1010px}.r5{top:1331px}.r6{top:1652px}.r7{top:1974px}.r8{top:2296px}
.abs{position:absolute}
.hl{color:var(--olive)}
.brand{position:absolute;color:var(--olive);line-height:1}
.brand .name{letter-spacing:.22em;font-weight:400}
.brand .tag{display:block;letter-spacing:.03em}
.brand-sm{right:10px;top:8px;text-align:right}
.brand-sm .name{font-size:12px}
.brand-sm .tag{font-size:5px;margin-top:2px}
.olive .brand{color:var(--white)}
.foot{position:absolute;left:13px;bottom:9px;font-size:5px;color:var(--ink)}
.page{position:absolute;right:16px;bottom:8px;font-size:7px;color:var(--ink)}
.olive .foot,.olive .page{color:var(--white)}
.photo{position:absolute}
/* cover */
.cover .brand{left:25px;top:34px}
.cover .brand .name{font-size:20px}
.cover .brand .tag{font-size:9px;margin-top:4px;padding-left:35px}
.cover-title{position:absolute;left:25px;top:137px;font-size:28px;line-height:30px;text-transform:uppercase}
.cover-sub{position:absolute;left:25px;top:198px;font-size:9.5px}
.cover-copy{position:absolute;left:25px;top:240px;font-size:7px}
.pill{position:absolute;border-radius:12px;text-align:center;font-size:8.5px}
.cover .pill{left:405px;top:234px;width:63px;height:22px;line-height:22px;background:var(--olive);color:var(--white)}
.olive.cover .pill{background:var(--white);color:var(--olive)}
.olive .hl{color:var(--white)}
/* agenda */
.agenda-title{position:absolute;top:40px;width:100%;text-align:center;font-size:20px}
.agenda-item{position:absolute;width:220px;height:34px}
.agenda-item .num{position:absolute;left:0;top:0;width:33px;height:33px;border:1px solid #c9cd9f;border-radius:50%;text-align:center;line-height:31px;color:var(--olive);font-size:12px}
.agenda-item h3{position:absolute;left:45px;top:-2px;font-weight:400;font-size:12px}
.agenda-item p{position:absolute;left:45px;top:18px;font-size:7px;white-space:nowrap}
/* title + band */
.slide-title{position:absolute;font-size:19px;font-weight:400;text-transform:uppercase}
.band{position:absolute;left:0;top:62px;width:510px;height:132px;background:var(--olive-pale)}
.lead-bold{position:absolute;font-weight:700;color:var(--olive);font-size:9px;line-height:15px}
.step{position:absolute;top:85px;width:95px;height:90px;background:var(--olive);color:var(--white);text-align:center;padding-top:12px}
.step b{display:block;font-size:15px}
.step strong{display:block;font-size:8.5px;margin:4px 0 3px}
.step span{display:block;font-size:6px;line-height:9px;padding:0 10px}
.small{font-size:7px;line-height:12px;color:#555}
/* section */
.frame{position:absolute;left:34px;top:34px;width:444px;height:216px;border:1px solid #e2e3dc}
.olive .frame{border-color:rgba(255,255,255,.35)}
.sec-num{position:absolute;right:50px;top:46px;font-size:78px;line-height:1;color:var(--olive)}
.olive .sec-num{color:var(--white)}
.sec-title{position:absolute;left:48px;top:158px;font-size:31px;line-height:35px}
.sec-text{position:absolute;right:53px;top:174px;width:150px;text-align:right;font-size:8.5px;line-height:13px}
/* text slides */
.statement{position:absolute;left:34px;top:76px;font-size:16px;line-height:18.5px;color:var(--olive)}
.tiny{font-size:6px;line-height:10px;color:#666}
.cols p{margin-bottom:9px}
/* collage */
.collage{position:absolute;inset:0;display:grid;grid-template-columns:repeat(7,1fr);grid-template-rows:repeat(6,1fr)}
.collage .ph{background:linear-gradient(135deg,#7d7f7a,#b9b4a6)}
.collage .ph.b{background:linear-gradient(135deg,#4d5866,#a3a7aa)}
.collage .ph.c{background:linear-gradient(135deg,#b3a27d,#e0ddd2)}
.collage .cn{background:var(--olive);color:var(--white);font-size:5.5px;font-weight:700;display:flex;align-items:center;justify-content:center}
.collage-box{position:absolute;left:158px;top:70px;width:186px;height:96px;background:var(--white);color:var(--ink);font-size:9px;font-weight:700;line-height:15.5px;text-align:center;display:flex;align-items:center;justify-content:center;padding:0 8px}
/* chart */
.bullets{position:absolute;left:34px;top:136px;list-style:none;font-size:7px;line-height:16.5px;color:#555}
.bullets li::before{content:"•";margin-right:6px}
.kpi{position:absolute;top:202px;width:97px;height:55px;color:var(--white);text-align:center;padding-top:10px}
.kpi b{display:block;font-size:17px}
.kpi span{display:block;font-size:6px;margin-top:5px}
/* products */
.products-title{position:absolute;left:0;top:18px;width:510px;text-align:center;font-size:20px;font-weight:400;text-transform:uppercase}
/* promise */
.promise-label{position:absolute;left:138px;top:60px;font-size:10px;color:#e2e5c8}
.promise{position:absolute;left:138px;top:82px;font-size:31px;line-height:36px}
.promise .dark{color:var(--olive-dark)}
/* quote */
.qmark{position:absolute;left:24px;top:50px;font-size:110px;line-height:1;color:#e6e8d5;font-weight:700;font-family:Georgia,serif}
.quote{position:absolute;left:63px;top:108px;font-size:18px;line-height:24px;text-transform:uppercase}
.author{position:absolute;left:66px;top:202px;padding-left:12px;border-left:2px solid var(--ink);font-size:9px;line-height:12px}
.author span{color:var(--olive);font-size:8px}
/* thank you */
.thanks .brand{left:37px;top:42px}
.thanks .brand .name{font-size:19px}
.thanks .brand .tag{font-size:8px;margin-top:4px;padding-left:33px}
.thanks h2{position:absolute;left:37px;top:132px;font-size:37px;font-weight:700}
.thanks .pill{left:37px;top:198px;width:118px;height:21px;line-height:21px;border-radius:3px;background:var(--olive);color:var(--white);letter-spacing:.08em}
</style>
</head>
<body>

<!-- Cover light -->
<section class="slide cover col-a r1">
  <div class="brand"><span class="name">NORVALE</span><span class="tag">Facility Solutions</span></div>
  <h1 class="cover-title" style="font-weight:400">Presentation title<br>text <span class="hl">goes here</span></h1>
  <p class="cover-sub">Lorem ipsum dolor sit amet consectetur</p>
  <p class="cover-copy">© Copyright 2025 | Norvale Facility Solutions</p>
  <div class="pill">May 2025</div>
</section>

<!-- Cover olive -->
<section class="slide olive cover col-b r1">
  <div class="brand"><span class="name">NORVALE</span><span class="tag">Facility Solutions</span></div>
  <h1 class="cover-title" style="font-weight:400;color:var(--olive-dark)">Presentation title<br>text <span style="color:var(--white)">goes here</span></h1>
  <p class="cover-sub">Lorem ipsum dolor sit amet consectetur</p>
  <p class="cover-copy">© Copyright 2025 | Norvale Facility Solutions</p>
  <div class="pill">May 2025</div>
</section>

<!-- Agenda -->
<section class="slide col-a r2">
  <div class="brand brand-sm"><span class="name">NORVALE</span><span class="tag">Facility Solutions</span></div>
  <h2 class="agenda-title" style="font-weight:400">OUR <span class="hl">AGENDA</span></h2>
  <div class="agenda-item" style="left:33px;top:91px"><div class="num">01</div><h3>Subtitle Text Here</h3><p>Lorem ipsum dolor sit amet dummy texts</p></div>
  <div class="agenda-item" style="left:33px;top:148px"><div class="num">02</div><h3>Subtitle Text Here</h3><p>Lorem ipsum dolor sit amet dummy texts</p></div>
  <div class="agenda-item" style="left:33px;top:203px"><div class="num">03</div><h3>Subtitle Text Here</h3><p>Lorem ipsum dolor sit amet dummy texts</p></div>
  <div class="agenda-item" style="left:258px;top:91px"><div class="num">04</div><h3>Subtitle Text Here</h3><p>Lorem ipsum dolor sit amet dummy texts</p></div>
  <div class="agenda-item" style="left:258px;top:148px"><div class="num">05</div><h3>Subtitle Text Here</h3><p>Lorem ipsum dolor sit amet dummy texts</p></div>
  <div class="agenda-item" style="left:258px;top:203px"><div class="num">06</div><h3>Subtitle Text Here</h3><p>Lorem ipsum dolor sit amet dummy texts</p></div>
  <p class="foot">© Copyright 2025 | Norvale Facility Solutions</p><p class="page">02</p>
</section>

<!-- Title + steps -->
<section class="slide col-b r2">
  <div class="brand brand-sm"><span class="name">NORVALE</span><span class="tag">Facility Solutions</span></div>
  <h2 class="slide-title" style="left:35px;top:28px">Enter <span class="hl">title here</span></h2>
  <div class="band"></div>
  <svg class="abs" style="left:28px;top:80px" width="20" height="26" viewBox="0 0 20 26" aria-hidden="true"><rect x="2" y="2" width="9" height="14" fill="none" stroke="#8a9440" stroke-width="2.4"/><rect x="9" y="8" width="9" height="10" fill="none" stroke="#8a9440" stroke-width="2.4"/><path d="M2 22h16" stroke="#8a9440" stroke-width="2.4"/></svg>
  <p class="lead-bold" style="left:29px;top:117px;width:145px">Lorem ipsum dolor sit amet dummy texts. Duis quis amet nunc vulputate dolor. Sceler ligula velit nulla faucibus</p>
  <div class="step" style="left:182px"><b>01</b><strong>Description</strong><span>Lorem ipsum dolor sit amet dummy texts. Duis quis amet nunc</span></div>
  <div class="step" style="left:285px"><b>02</b><strong>Description</strong><span>Lorem ipsum dolor sit amet dummy texts. Duis quis amet nunc</span></div>
  <div class="step" style="left:387px"><b>03</b><strong>Description</strong><span>Lorem ipsum dolor sit amet dummy texts. Duis quis amet nunc</span></div>
  <svg class="abs" style="left:28px;top:213px" width="20" height="20" viewBox="0 0 20 20" aria-hidden="true"><rect x="1" y="12" width="4" height="8" fill="#8a9440"/><rect x="7" y="9" width="4" height="11" fill="#8a9440"/><rect x="13" y="6" width="4" height="14" fill="#8a9440"/><path d="M1 9 L8 4 L12 7 L19 1" stroke="#8a9440" stroke-width="2" fill="none"/></svg>
  <div class="abs" style="left:57px;top:208px;width:1px;height:32px;background:#ccc"></div>
  <p class="abs small" style="left:68px;top:208px;width:420px;font-size:6.5px;line-height:12px">Lorem ipsum dolor sit amet dummy texts. Duis quis amet nunc vulputate dolor. Scelerisque ligula velit nulla faucibus donec pellentesque massa mi. Aliquam in fusce semper aliquam egestas mauris est nunc. Et pellentesque sodales elementum cursus mattis suscipit etiam nulla odio. Molestie tristique cursus</p>
  <p class="foot">© Copyright 2025 | Norvale Facility Solutions</p><p class="page">02</p>
</section>

<!-- Section 01 -->
<section class="slide col-a r3">
  <div class="brand brand-sm"><span class="name">NORVALE</span><span class="tag">Facility Solutions</span></div>
  <div class="frame"></div>
  <div class="sec-num">01</div>
  <h2 class="sec-title" style="font-weight:400">SECTION<br><span class="hl">SLIDES</span></h2>
  <p class="sec-text">Lorem ipsum dolor sit amet dummy texts. Duis quis amet nunc vulputate dolor scelerisque ligula.</p>
  <p class="foot">© Copyright 2025 | Norvale Facility Solutions</p><p class="page">02</p>
</section>

<!-- Section 02 -->
<section class="slide olive col-b r3">
  <div class="brand brand-sm"><span class="name">NORVALE</span><span class="tag">Facility Solutions</span></div>
  <div class="frame"></div>
  <div class="sec-num">02</div>
  <h2 class="sec-title" style="font-weight:400;color:var(--olive-dark)">SECTION<br><span style="color:var(--white)">SLIDES</span></h2>
  <p class="sec-text">Lorem ipsum dolor sit amet dummy texts. Duis quis amet nunc vulputate dolor scelerisque ligula.</p>
  <p class="foot">© Copyright 2025 | Norvale Facility Solutions</p><p class="page">02</p>
</section>

<!-- Statement + photo -->
<section class="slide col-a r4">
  <p class="statement">Lorem ipsum<br>dolor sit amet<br>dummy texts.<br>Duissuis amet<br>nunces sets</p>
  <p class="abs tiny" style="left:34px;top:173px;width:118px">Lorem ipsum dolor sit amet dummy texts. Duis quis amet nunc vulputate dolor. Scelerisque ligula velit nulla fauci donec.</p>
  <div class="photo" role="img" aria-label="Photo of a chef flambéing a pan in a commercial restaurant kitchen" style="left:164px;top:0;width:346px;height:287px;background:linear-gradient(135deg,#3f3a33 0%,#8a7a62 45%,#d98a2e 62%,#5b554c 100%)"></div>
  <div class="brand brand-sm"><span class="name">NORVALE</span><span class="tag">Facility Solutions</span></div>
  <p class="foot">© Copyright 2025 | Norvale Facility Solutions</p>
</section>

<!-- Text columns -->
<section class="slide col-b r4">
  <div class="brand brand-sm"><span class="name">NORVALE</span><span class="tag">Facility Solutions</span></div>
  <p class="lead-bold" style="left:24px;top:56px;width:140px;font-size:8.5px;line-height:14px">Lorem ipsum dolor sit amet dummy texts. Duis quis amet nu vulputate dolor. Sceleri ligula velit nulla faucibus donec pellentesque massa miesat. Aliquam in fusce semper aliqua egestas mauris est nunc.</p>
  <div class="abs tiny cols" style="left:197px;top:58px;width:122px;color:#333">
    <p>Lorem ipsum dolor sit amet dummy texts. Duis quis amet nunc vulputate dolor. Scelerisque ligula velit nulla fauci donec pellentesque massa mi. Aliquam in fusce semper aliquam egestas mauris est nunc. Et pellentese sodales elemen tum cursus mattis suscipit etiam.</p>
    <p>Molestie tristique cursus ipsum non vitae nibh amet lacus. Orci dictum erat vitae at at non massa. Sit sit nisl pretium quisque ornare nunc posuere nunc. Et at est varius pulvinar sodales massa pulvinar risus. Orci at ipsum tellus posuere nunc. Auctor malesuada plac.</p>
  </div>
  <div class="abs tiny cols" style="left:336px;top:58px;width:122px;color:#333">
    <p>Eget libero aliquet hendrerit et tellus aliquam enim proin elementum. Enim purus nulla nunc accumsan suspen disse gravida dolor nulla. Eget diam elit rhoncus dui integer egestas. Eget sagittis tortor arcu id nec eu integer morbi risus posuere egestas ac.</p>
    <p>Penatibus imperdiet adipiscing rhoncus blandit tortor in. Tortor sagittis massa adipiscing in at nam placerat tincidunt. Ut interdum integer senectus a sapien. Tortor magna velit ut non. Tellus massa etiam vel elementum varius in leo. Vitae id magna laoreet mauris.</p>
  </div>
  <p class="foot">© Copyright 2025 | Norvale Facility Solutions</p><p class="page">02</p>
</section>

<!-- Two-line title + band -->
<section class="slide col-a r5">
  <div class="brand brand-sm"><span class="name">NORVALE</span><span class="tag">Facility Solutions</span></div>
  <h2 class="slide-title" style="left:34px;top:22px;font-size:17px;line-height:19px">Enter your two-line<br><span class="hl">title here</span></h2>
  <p class="abs tiny" style="left:34px;top:66px;width:190px">Lorem ipsum dolor sit amet dummy texts. Duis quis amet nunc vulputate dolor. Scelerisque ligula velit nulla fauci donec.</p>
  <div class="abs" style="left:0;top:98px;width:182px;height:162px;background:var(--olive);color:var(--white);padding:28px 12px 0 34px">
    <p style="font-size:10px;line-height:12px">Lorem ipsum dolor sit amet dummy texts duis</p>
    <p style="font-size:5.5px;line-height:10px;margin-top:6px">Lorem ipsum dolor sit amet dummy texts. Duis quis amet nunc vulputate dolor. Scelerisque ligula velit nulla faucibus donec pellentesque massa mi. Aliquam in fusce semper aliquam egestas mauris est nunc. Et pellentesque soda elementum cursus mattis suscipit etiam nulla odio. Molestie tristique cursus ipsum non vitae nibh amet lacus erci dictum erat.</p>
  </div>
  <div class="photo" role="img" aria-label="Photo of a family shopping for fresh produce in a grocery store" style="left:182px;top:98px;width:328px;height:162px;background:linear-gradient(120deg,#8d5b3a 0%,#d8a066 35%,#c9c2b2 60%,#9b6a3f 100%)"></div>
  <p class="foot">© Copyright 2025 | Norvale Facility Solutions</p><p class="page">02</p>
</section>

<!-- Client collage -->
<section class="slide col-b r5">
  <div class="collage" role="img" aria-label="Grid of photos of technicians, kitchens and stores alternating with client name tiles">
    <div class="ph"></div><div class="cn">Client Name</div><div class="ph c"></div><div class="ph b"></div><div class="cn">Client Name</div><div class="ph c"></div><div class="cn">Client Name</div>
    <div class="ph c"></div><div class="ph b"></div><div class="cn">Client Name</div><div class="ph b"></div><div class="ph"></div><div class="cn">Client Name</div><div class="ph c"></div>
    <div class="cn">Client Name</div><div class="ph b"></div><div class="ph"></div><div class="ph"></div><div class="ph"></div><div class="ph b"></div><div class="ph"></div>
    <div class="ph"></div><div class="cn">Client Name</div><div class="ph"></div><div class="ph"></div><div class="ph"></div><div class="ph c"></div><div class="cn">Client Name</div>
    <div class="ph c"></div><div class="ph b"></div><div class="cn">Client Name</div><div class="ph"></div><div class="ph b"></div><div class="cn">Client Name</div><div class="ph"></div>
    <div class="cn">Client Name</div><div class="ph b"></div><div class="ph c"></div><div class="cn">Client Name</div><div class="ph"></div><div class="ph c"></div><div class="ph b"></div>
  </div>
  <div class="collage-box">Lorem ipsum dolor sit amet dummy texts. Duis quis amet nu vulputate dolor. Sceleri ligula velit nulla faucibus donec pellentesque massa miesat.</div>
</section>

<!-- Bar chart -->
<section class="slide col-a r6">
  <div class="brand brand-sm"><span class="name">NORVALE</span><span class="tag">Facility Solutions</span></div>
  <h2 class="slide-title" style="left:34px;top:48px;font-size:19px;line-height:22px">Enter your<br><span class="hl">title here</span></h2>
  <p class="abs tiny" style="left:34px;top:100px;width:180px">Lorem ipsum dolor sit amet dummy texts. Duis quis amet nunc vulputate dolor. Scelerisque ligula velit nulla fauci donec.</p>
  <ul class="bullets">
    <li>Duis quis amet nunc vulputate dolor.</li>
    <li>Scelerisque ligula velit nulla faucibus donec</li>
    <li>Pellentesque massa mi aliquam in fusce</li>
    <li>Semper aliquam egestas mauris est nunc</li>
    <li>Et pellentesque sodales elemenrsus</li>
    <li>Mattis suscipit etiam nulla odio molestie</li>
  </ul>
  <svg class="abs" style="left:255px;top:30px" width="220" height="170" viewBox="0 0 220 170" aria-label="Bar chart, years 1 to 5">
    <g font-size="5" fill="#333" text-anchor="end" font-family="Arimo,Arial,sans-serif">
      <text x="10" y="9">100</text><text x="10" y="38">80</text><text x="10" y="67">60</text><text x="10" y="96">40</text><text x="10" y="125">20</text><text x="10" y="154">0</text>
    </g>
    <line x1="15" y1="7" x2="15" y2="152" stroke="#999" stroke-width=".6"/>
    <line x1="15" y1="152" x2="212" y2="152" stroke="#999" stroke-width=".6"/>
    <rect x="22" y="22" width="33" height="130" fill="#8a9440"/>
    <rect x="61" y="51" width="33" height="101" fill="#7b7b7b"/>
    <rect x="100" y="87" width="33" height="65" fill="#8a9440"/>
    <rect x="139" y="68" width="33" height="84" fill="#7b7b7b"/>
    <rect x="178" y="47" width="33" height="105" fill="#8a9440"/>
    <g font-size="5" fill="#333" text-anchor="middle" font-family="Arimo,Arial,sans-serif">
      <text x="38" y="159">Year 1</text><text x="77" y="159">Year 2</text><text x="116" y="159">Year 3</text><text x="155" y="159">Year 4</text><text x="194" y="159">Year 5</text>
    </g>
  </svg>
  <div class="kpi" style="left:263px;background:var(--olive)"><b>Year 2</b><span>Profitability</span></div>
  <div class="kpi" style="left:367px;background:var(--grey)"><b>20%</b><span>Gross margin</span></div>
  <p class="foot">© Copyright 2025 | Norvale Facility Solutions</p><p class="page">02</p>
</section>

<!-- Products ring -->
<section class="slide col-b r6">
  <svg class="abs" style="left:0;top:0" width="510" height="287" viewBox="0 0 510 287" aria-label="Ring diagram of five product lines">
    <g transform="translate(5,-3)" stroke="#fff" stroke-width="3">
      <path d="M154.9 134.1 A100 100 0 0 1 250 65 L250 120 A45 45 0 0 0 207.2 151.1 Z" fill="#9a9a9a"/>
      <path d="M250 65 A100 100 0 0 1 345.1 134.1 L292.8 151.1 A45 45 0 0 0 250 120 Z" fill="#d9d9d9"/>
      <path d="M345.1 134.1 A100 100 0 0 1 308.8 245.9 L276.5 201.4 A45 45 0 0 0 292.8 151.1 Z" fill="#e2e5cf"/>
      <path d="M308.8 245.9 A100 100 0 0 1 191.2 245.9 L223.5 201.4 A45 45 0 0 0 276.5 201.4 Z" fill="#c6cb9c"/>
      <path d="M191.2 245.9 A100 100 0 0 1 154.9 134.1 L207.2 151.1 A45 45 0 0 0 223.5 201.4 Z" fill="#8a9440"/>
    </g>
    <g transform="translate(5,-3)" font-family="Arimo,Arial,sans-serif" font-size="10" text-anchor="middle" fill="#333">
      <text x="207.7" y="110">01</text><text x="292.3" y="110">02</text><text x="318.5" y="190">03</text><text x="250" y="240">04</text><text x="181.5" y="190" fill="#fff">05</text>
      <text x="250" y="160" font-size="12">OUR</text><text x="250" y="177" font-size="12" fill="#8a9440">PRODUCTS</text>
    </g>
    <g stroke="#555" stroke-width=".6" fill="none">
      <path d="M124 65 H180 L200 84"/><path d="M370 80 H338 L318 98"/>
      <path d="M108 170 H152"/><path d="M378 222 H340 L322 206"/><path d="M148 253 H222"/>
    </g>
    <g font-family="Arimo,Arial,sans-serif" font-size="8" fill="#333">
      <text x="94" y="68">HVAC</text><text x="374" y="83">Refrigeration</text>
      <text x="70" y="170">Food</text><text x="58" y="181">Equipment</text>
      <text x="382" y="225">Plumbing</text><text x="108" y="256">Electrical</text>
    </g>
  </svg>
  <h2 class="products-title">Enter <span class="hl">title here</span></h2>
  <div class="brand brand-sm"><span class="name">NORVALE</span><span class="tag">Facility Solutions</span></div>
  <p class="foot">© Copyright 2025 | Norvale Facility Solutions</p><p class="page">02</p>
</section>

<!-- Full photo statement -->
<section class="slide col-a r7">
  <div class="photo" role="img" aria-label="Photo of an electrician in a hard hat and safety glasses working on a wiring panel" style="inset:0;background:linear-gradient(90deg,#3e4230 0%,#59593f 45%,#6b6a5c 70%,#2f3437 100%)"></div>
  <p class="abs" style="left:47px;top:128px;font-size:24px;line-height:28px;color:var(--white)">Lorem ipsum dolor<br>sit amet dummy<br>texts. Duissuis amet<br>nunces sets</p>
</section>

<!-- Promise -->
<section class="slide olive col-b r7">
  <div class="brand brand-sm"><span class="name">NORVALE</span><span class="tag">Facility Solutions</span></div>
  <p class="promise-label">OUR PROMISE:</p>
  <p class="promise">Spend less.<br>Strees less.<br><span class="dark">One work order<br>at a time.</span></p>
  <p class="foot">© Copyright 2025 | Norvale Facility Solutions</p><p class="page">02</p>
</section>

<!-- Quote -->
<section class="slide col-a r8">
  <div class="brand brand-sm"><span class="name">NORVALE</span><span class="tag">Facility Solutions</span></div>
  <div class="qmark">“</div>
  <p class="quote">Lorem ipsum dolor sit amet dummy<br>texts. Duis quis amet nunc vultate<br>dolor scelerisque ligula.</p>
  <p class="author">Dr. Dana Morrow<br><span>CEO / Founder</span></p>
  <p class="foot">© Copyright 2025 | Norvale Facility Solutions</p><p class="page">02</p>
</section>

<!-- Thank you -->
<section class="slide thanks col-b r8">
  <div class="brand"><span class="name">NORVALE</span><span class="tag">Facility Solutions</span></div>
  <h2>THANK <span class="hl">YOU</span></h2>
  <div class="pill">www.norvaleurl.com</div>
</section>

</body>
</html>
```